eCommerce website for a DIY shop & communal center

We need a website for a business called The Makerloft Barn. The Makerloft Barn is both a shop and communal establishment where people with shared interests, especially in DIY (Do It Yourself) and crafting, can gather to shop for & work on projects while sharing ideas, equipment, supplies and knowledge. The shop is both brick & motor and online. The physical communal space provides workstations, equipment, tools and supplies and expertise for DIY lovers to create their projects.

Target Market(s)

Middle & upper class DIY enthusiasts, creative hobbyists, budding artists & small business owners

Industry/Entity Type

DIY, Arts & Crafts

Coding

Coded - Design and coding required

Number of Pages Required

5+ page

Requirements
Must have
• Menus to include 1. home page (with about us, operating hours, contacts, location, meet the team); 2. Studio activities (how to DIY at the Studio, booking, equipment & tools, house rules); 3. Studio events (events in the Studio, offsite events); 4. Resources (FAQs, tutorials, blogs, eBooks) and 5. Online shop
Nice to have
• Branding guidelines eg logo colours (see attachment) to influence design. Woo commerce shop. Booking feature for activities & events at the Studio.

```html
<!DOCTYPE html>
<html lang="en">
<head>
<meta charset="utf-8">
<title>The Makerloft Barn</title>
<link href="https://fonts.googleapis.com/css2?family=Roboto+Slab:wght@400;500;700&display=swap" rel="stylesheet">
<style>
:root{
  --orange:#f0782f;
  --blue:#2d95d3;
  --peach:#fcd3bf;
  --sky:#d2e8f5;
  --pink:#f9d4e2;
  --mist:#f7f7f8;
  --ink:#1d1d1d;
  --text:#333;
  --muted:#666;
  --night:#141414;
  --white:#fff;
}
*{box-sizing:border-box;margin:0;padding:0}
html,body{width:1200px;height:4054px;overflow:hidden}
body{font-family:"Roboto Slab",serif;color:var(--text);background:var(--white);position:relative}
.abs{position:absolute}
.band{position:absolute;left:0;width:1200px}
a{color:inherit;text-decoration:none}

/* header */
.site-header{position:absolute;top:0;left:0;width:1200px;height:107px;background:var(--white);z-index:3}
.brand-box{position:absolute;left:88px;top:0;width:192px;height:145px;background:var(--white);border-left:8px solid var(--orange);border-bottom:8px solid var(--orange);box-shadow:0 4px 12px rgba(0,0,0,.12);display:flex;align-items:center;justify-content:center;z-index:4}
.brand-name{font-weight:700;font-size:22px;line-height:1.15;color:var(--orange);text-align:center}
.contact-phone{position:absolute;left:822px;top:22px;display:flex;align-items:center;gap:10px}
.icon-square{width:28px;height:28px;border:1.5px solid #bbb;border-radius:4px;display:flex;align-items:center;justify-content:center}
.phone-label{font-size:11px;color:var(--muted);line-height:1.2}
.phone-num{font-size:14px;color:var(--orange);font-weight:500}
.search-btn{position:absolute;left:983px;top:22px}
.cart{position:absolute;left:1034px;top:18px}
.cart-count{position:absolute;left:1080px;top:20px;width:30px;height:30px;border-radius:50%;background:var(--orange);color:#fff;font-size:13px;font-weight:700;display:flex;align-items:center;justify-content:center}
.main-nav{position:absolute;top:71px;left:554px;font-size:14px;font-weight:500;color:var(--ink)}
.main-nav a{position:absolute;white-space:nowrap}
.main-nav .active{color:var(--orange);text-decoration:underline}

/* hero */
.hero{position:absolute;top:107px;left:0;width:1200px;height:560px;background:linear-gradient(100deg,#6b4b32 0%,#3a3a3a 30%,#2a2f36 60%,#18191c 100%)}
.hero-title{position:absolute;top:272px;left:0;width:1200px;text-align:center}
.hero-kicker{font-size:31px;font-weight:700;color:var(--orange)}
.hero-head{font-size:57px;font-weight:700;color:var(--blue);line-height:1.15;margin-top:6px}
.btn{display:inline-flex;align-items:center;justify-content:center;font-size:14px;border:2px solid var(--orange);color:var(--orange);border-radius:3px;background:var(--white)}
.btn-ghost{background:transparent}
.btn-solid{background:var(--blue);border-color:var(--blue);color:#fff}
.hero-cta{position:absolute;left:532px;top:397px;width:136px;height:34px}
.slider-dot{position:absolute;top:588px;width:22px;height:22px;border-radius:50%;display:flex;align-items:center;justify-content:center}

/* shared */
.section-title{font-size:34px;font-weight:700;color:var(--orange)}
.center{text-align:center;width:1200px;left:0}
.body-copy{font-size:13px;line-height:20px;color:var(--text)}
.photo{position:absolute}
.frame{position:absolute;background:var(--white);box-shadow:0 4px 16px rgba(0,0,0,.14);padding:8px}
.frame .photo{position:static;width:100%;height:100%}
.meta{display:flex;align-items:center;gap:18px;font-size:12px;color:var(--ink)}
.meta span{display:flex;align-items:center;gap:7px}

/* events */
.event-card{position:absolute;top:2025px;width:325px;height:367px;background:var(--white);border:1px solid #e5e5e5}
.event-card .photo{left:0;top:0;width:100%;height:189px}
.event-tag{position:absolute;left:28px;top:177px;width:70px;height:25px;background:var(--orange);color:#fff;font-size:13px;font-weight:700;display:flex;align-items:center;justify-content:center}
.event-card .meta{position:absolute;left:28px;top:230px}
.event-card h3{position:absolute;left:28px;top:273px;width:270px;font-size:19px;line-height:26px;font-weight:700;color:var(--ink)}
.event-card.hover h3{color:var(--orange)}

/* resources */
.resource{position:absolute;top:2751px;width:208px;height:186px;background:var(--white);text-align:center}
.resource.raised{box-shadow:0 4px 16px rgba(0,0,0,.1)}
.resource svg{position:absolute;left:70px;top:40px}
.resource h3{position:absolute;top:132px;width:100%;font-size:22px;font-weight:700;color:var(--orange)}

/* products */
.product{position:absolute;top:3276px;width:231px;text-align:center}
.product .photo{position:relative;width:231px;height:231px;border:1px solid #e3e3e3}
.product-name{margin-top:14px;font-size:14px;color:var(--ink);line-height:19px}
.product-price{font-size:14px;color:var(--orange);font-weight:500;margin-top:4px}
.add-cart{position:absolute;left:57px;top:95px;width:117px;height:34px;background:var(--blue);color:#fff;font-size:13px;display:flex;align-items:center;justify-content:center;border-radius:3px}

/* footer */
.footer-col{position:absolute;top:3760px;font-size:14px;color:#eee;line-height:30px}
.footer-col h4{font-size:17px;color:var(--orange);font-weight:700;margin-bottom:8px}
.footer-brand{position:absolute;left:88px;top:3800px;font-size:30px;font-weight:700;color:var(--orange);line-height:1.15}
.social{display:flex;gap:9px;margin-top:10px}
.social i{width:26px;height:26px;border:1.5px solid #ddd;border-radius:50%;display:block}
.copyright{position:absolute;left:0;top:4013px;width:1200px;height:41px;background:var(--orange);color:#fff;font-size:13px;display:flex;align-items:center;justify-content:center}
</style>
</head>
<body>

<header class="site-header">
  <div class="brand-box"><div class="brand-name">The Makerloft<br>Barn</div></div>
  <div class="contact-phone">
    <div class="icon-square"><svg width="14" height="14" viewBox="0 0 24 24"><path d="M6.6 10.8a15 15 0 006.6 6.6l2.2-2.2c.3-.3.7-.4 1-.2 1.1.4 2.3.6 3.6.6.6 0 1 .4 1 1V20c0 .6-.4 1-1 1A17 17 0 013 4c0-.6.4-1 1-1h3.5c.6 0 1 .4 1 1 0 1.2.2 2.4.6 3.6.1.3 0 .7-.2 1z" fill="#888"/></svg></div>
    <div><div class="phone-label">Phone</div><div class="phone-num">555-014-2290</div></div>
  </div>
  <div class="search-btn icon-square"><svg width="14" height="14" viewBox="0 0 24 24" fill="none" stroke="#555" stroke-width="2.5"><circle cx="10" cy="10" r="6"/><path d="M15 15l5 5"/></svg></div>
  <svg class="cart" width="38" height="34" viewBox="0 0 38 34" fill="none" stroke="#666" stroke-width="2.2"><path d="M2 12h34l-4 19H6z"/><path d="M10 12l7-9M28 12l-7-9"/><path d="M13 17v9M19 17v9M25 17v9"/></svg>
  <div class="cart-count">00</div>
  <nav class="main-nav">
    <a class="active" style="left:0">Home</a>
    <a style="left:79px">Studio Activities</a>
    <a style="left:232px">Studio Events</a>
    <a style="left:366px">Resources</a>
    <a style="left:474px">Online Shop</a>
  </nav>
</header>

<section class="hero">
  <div class="photo" role="img" aria-label="Close-up of a hand painting a sunset scene on a wooden slice" style="inset:0;background:linear-gradient(95deg,rgba(214,120,40,.55) 0%,rgba(60,90,120,.35) 35%,rgba(0,0,0,.5) 70%,rgba(0,0,0,.75) 100%)"></div>
  <div class="hero-title" style="top:165px">
    <div class="hero-kicker">Welcome to</div>
    <div class="hero-head">The Makerloft Barn</div>
  </div>
  <a class="btn btn-ghost hero-cta" style="top:290px">Contact Us</a>
  <div class="slider-dot" style="left:124px;top:481px;background:rgba(255,255,255,.35)"><svg width="12" height="12" viewBox="0 0 12 12" fill="none" stroke="#333" stroke-width="2"><path d="M10 6H2M5 3L2 6l3 3"/></svg></div>
  <div class="slider-dot" style="left:153px;top:481px;background:var(--blue)"><svg width="12" height="12" viewBox="0 0 12 12" fill="none" stroke="#fff" stroke-width="2"><path d="M2 6h8M7 3l3 3-3 3"/></svg></div>
</section>
<svg class="band" style="top:540px" width="1200" height="140" viewBox="0 0 1200 140" preserveAspectRatio="none">
  <polygon points="0,105 1200,10 1200,140 0,140" fill="var(--peach)"/>
  <polygon points="0,135 1200,30 1200,140 0,140" fill="#fff"/>
</svg>

<!-- about -->
<h2 class="section-title abs" style="left:88px;top:760px">About Us</h2>
<p class="abs" style="left:88px;top:829px;width:430px;font-size:15px;line-height:21px;font-weight:700;color:var(--ink)">Hello!&nbsp; Welcome to The Makerloft Barn!&nbsp; I am so glad you're here..truly I am!</p>
<div class="abs body-copy" style="left:88px;top:891px;width:435px">
  <p>Most of our friends know me as the Crate Lady from Sawdust Notes. I'm still the same Crate Lady, we've just expanded from a blog up on a hill to a full service DIY studio in Millbrook, Kentucky.</p>
  <p style="margin-top:20px">My heart and my vision has not changed just expanded.</p>
  <p style="margin-top:20px">Since our very humble beginnings in our basement; we have since grown to a corporation...</p>
</div>
<a class="btn abs" style="left:88px;top:1087px;width:136px;height:35px">Read More</a>
<a class="btn abs" style="left:241px;top:1087px;width:164px;height:35px">Meet The Team</a>
<div class="frame" style="left:682px;top:732px;width:428px;height:419px"><div class="photo" role="img" aria-label="Children and staff working on craft projects at a patterned table" style="background:linear-gradient(135deg,#c9a95a 0%,#6a6a5a 40%,#5a74b0 75%,#e7873a 100%)"></div></div>
<div class="frame" style="left:619px;top:918px;width:205px;height:218px"><div class="photo" role="img" aria-label="Girl holding up her painted wooden slice" style="background:linear-gradient(160deg,#5e8a4a 0%,#3a3a3a 55%,#d8742f 100%)"></div></div>

<!-- activities -->
<svg class="band" style="top:1240px" width="1200" height="90" viewBox="0 0 1200 90" preserveAspectRatio="none">
  <polygon points="0,0 1200,55 1200,90 0,90" fill="var(--sky)"/>
  <polygon points="0,18 1200,82 1200,90 0,90" fill="var(--mist)"/>
</svg>
<div class="abs" style="left:0;top:1328px;width:1200px;height:480px;background:var(--mist)"></div>
<div class="frame" style="left:88px;top:1405px;width:344px;height:312px"><div class="photo" role="img" aria-label="Child painting a canvas at an easel" style="background:linear-gradient(120deg,#6e86c4 0%,#e9e4dc 40%,#d3772e 65%,#3a2c2a 100%)"></div></div>
<h2 class="section-title abs" style="left:488px;top:1414px">Studio activities</h2>
<div class="meta abs" style="left:490px;top:1474px">
  <span><svg width="16" height="16" viewBox="0 0 16 16" fill="none" stroke="var(--orange)" stroke-width="1.5"><rect x="1.5" y="3" width="13" height="11.5" rx="1"/><path d="M1.5 6.5h13M5 1v4M11 1v4"/></svg>08/10/2021</span>
  <span><svg width="14" height="16" viewBox="0 0 14 16"><path d="M7 0a6 6 0 00-6 6c0 4.5 6 10 6 10s6-5.5 6-10a6 6 0 00-6-6zm0 8.5A2.5 2.5 0 117 3.5a2.5 2.5 0 010 5z" fill="var(--orange)"/></svg>Millbrook, KY</span>
</div>
<div class="abs body-copy" style="left:490px;top:1510px;width:585px">
  <p>Lorem Ipsum is simply dummy text of the printing and typesetting industry. Lorem Ipsum has been the industry's standard dummy text ever since the 1500s, when an unknown printer took a galley of type and scrambled it to make a type specimen book.</p>
  <p style="margin-top:18px">It has survived not only five centuries, but also the leap into electronic typesetting, remaining essentially unchanged. It was popularised...</p>
</div>
<a class="btn abs" style="left:490px;top:1655px;width:136px;height:35px">Read More</a>
<a class="btn btn-solid abs" style="left:643px;top:1655px;width:129px;height:35px">Book Now</a>
<svg class="band" style="top:1790px" width="1200" height="90" viewBox="0 0 1200 90" preserveAspectRatio="none">
  <polygon points="0,0 1200,0 1200,5 0,60" fill="var(--mist)"/>
  <polygon points="0,60 1200,5 1200,30 0,85" fill="var(--pink)"/>
</svg>

<!-- events -->
<h2 class="section-title abs center" style="top:1926px">Studio Events</h2>
<div class="abs center" style="top:1976px;font-size:14px">
  <span style="color:var(--blue);text-decoration:underline;margin-right:20px">In the Studio</span><span style="color:var(--muted)">Offsite Events</span>
</div>
<article class="event-card" style="left:88px">
  <div class="photo" role="img" aria-label="Painting of a seaside scene on an easel" style="background:linear-gradient(120deg,#e0a44a 0%,#7c92b8 45%,#4d6a8e 70%,#f0c06a 100%)"></div>
  <span class="event-tag">Art</span>
  <div class="meta"><span><svg width="16" height="16" viewBox="0 0 16 16" fill="none" stroke="var(--orange)" stroke-width="1.5"><rect x="1.5" y="3" width="13" height="11.5" rx="1"/><path d="M1.5 6.5h13M5 1v4M11 1v4"/></svg>08/10/2021</span><span><svg width="14" height="16" viewBox="0 0 14 16"><path d="M7 0a6 6 0 00-6 6c0 4.5 6 10 6 10s6-5.5 6-10a6 6 0 00-6-6zm0 8.5A2.5 2.5 0 117 3.5a2.5 2.5 0 010 5z" fill="var(--orange)"/></svg>Millbrook, KY</span></div>
  <h3>Lorem Ipsum is simply dummy text of the printing and typesetting industry.</h3>
</article>
<article class="event-card" style="left:438px">
  <div class="photo" role="img" aria-label="Group of children in aprons cheering at an event" style="background:linear-gradient(160deg,#e6d2c0 0%,#c13a3a 45%,#e9c53a 75%,#3a5ea8 100%)"></div>
  <span class="event-tag">Art</span>
  <div class="meta"><span><svg width="16" height="16" viewBox="0 0 16 16" fill="none" stroke="var(--orange)" stroke-width="1.5"><rect x="1.5" y="3" width="13" height="11.5" rx="1"/><path d="M1.5 6.5h13M5 1v4M11 1v4"/></svg>08/10/2021</span><span><svg width="14" height="16" viewBox="0 0 14 16"><path d="M7 0a6 6 0 00-6 6c0 4.5 6 10 6 10s6-5.5 6-10a6 6 0 00-6-6zm0 8.5A2.5 2.5 0 117 3.5a2.5 2.5 0 010 5z" fill="var(--orange)"/></svg>Millbrook, KY</span></div>
  <h3>Lorem Ipsum is simply dummy text of the printing and typesetting industry.</h3>
</article>
<article class="event-card hover" style="left:788px">
  <div class="photo" role="img" aria-label="Wooden dartboard cabinet built from pallet wood" style="background:linear-gradient(120deg,#d9c2a3 0%,#c9ab84 50%,#8b7a66 100%)"></div>
  <span class="event-tag">Art</span>
  <div class="meta"><span><svg width="16" height="16" viewBox="0 0 16 16" fill="none" stroke="var(--orange)" stroke-width="1.5"><rect x="1.5" y="3" width="13" height="11.5" rx="1"/><path d="M1.5 6.5h13M5 1v4M11 1v4"/></svg>08/10/2021</span><span><svg width="14" height="16" viewBox="0 0 14 16"><path d="M7 0a6 6 0 00-6 6c0 4.5 6 10 6 10s6-5.5 6-10a6 6 0 00-6-6zm0 8.5A2.5 2.5 0 117 3.5a2.5 2.5 0 010 5z" fill="var(--orange)"/></svg>Millbrook, KY</span></div>
  <h3>Lorem Ipsum is simply dummy text of the printing and typesetting industry.</h3>
</article>
<a class="btn abs" style="left:532px;top:2435px;width:136px;height:35px">View More</a>

<!-- resources -->
<svg class="band" style="top:2520px" width="1200" height="90" viewBox="0 0 1200 90" preserveAspectRatio="none">
  <polygon points="0,0 1200,40 1200,90 0,90" fill="var(--peach)"/>
  <polygon points="0,18 1200,60 1200,90 0,90" fill="var(--mist)"/>
</svg>
<div class="abs" style="left:0;top:2605px;width:1200px;height:460px;background:var(--mist)"></div>
<h2 class="section-title abs center" style="top:2668px">Resources</h2>
<div class="resource" style="left:145px">
  <svg width="68" height="64" viewBox="0 0 68 64" fill="none" stroke="#333" stroke-width="2"><path d="M26 6h34a4 4 0 014 4v22a4 4 0 01-4 4h-6l-6 8v-8H26a4 4 0 01-4-4V10a4 4 0 014-4z"/><path d="M39 16a4 4 0 117 3c-2 1-3 2-3 4M43 28v1"/><path d="M18 22H8a4 4 0 00-4 4v20a4 4 0 004 4h4v8l8-8h14a4 4 0 004-4v-6"/><path d="M12 36h2M20 36h2M28 36h2"/></svg>
  <h3>FAQs</h3>
</div>
<div class="resource" style="left:386px">
  <svg width="68" height="64" viewBox="0 0 68 64" fill="none" stroke="#333" stroke-width="2"><rect x="6" y="8" width="56" height="40" rx="2"/><path d="M6 42h56M4 54h60"/><circle cx="34" cy="25" r="9"/><path d="M31 20l7 5-7 5z"/></svg>
  <h3>Tutorials</h3>
</div>
<div class="resource raised" style="left:627px">
  <svg width="68" height="64" viewBox="0 0 68 64" fill="none" stroke="#333" stroke-width="2"><path d="M46 36v22H8V6h38v8"/><path d="M16 16h22M16 24h18M16 32h14M16 40h12M16 48h20"/><path d="M60 10l4 4-22 22-6 2 2-6z"/></svg>
  <h3>Blogs</h3>
</div>
<div class="resource" style="left:868px">
  <svg width="68" height="64" viewBox="0 0 68 64" fill="none" stroke="#333" stroke-width="2"><rect x="16" y="4" width="26" height="54" rx="4"/><path d="M26 52h6"/><path d="M26 18h28v24H26z"/><path d="M40 18v24M30 24h6M30 30h6M44 24h6M44 30h6"/><path d="M14 30c-4 2-6 6-6 10"/></svg>
  <h3>eBooks</h3>
</div>

<!-- products -->
<svg class="band" style="top:3045px" width="1200" height="90" viewBox="0 0 1200 90" preserveAspectRatio="none">
  <polygon points="0,0 1200,0 1200,2 0,60" fill="var(--mist)"/>
  <polygon points="0,60 1200,2 1200,20 0,82" fill="var(--sky)"/>
</svg>
<h2 class="section-title abs center" style="top:3190px">Latest Products</h2>
<div class="product" style="left:88px">
  <div class="photo" role="img" aria-label="Jars of chalky paint beside a letter board" style="background:linear-gradient(150deg,#2b2b2b 0%,#4a4038 50%,#b0322a 80%,#c9b79a 100%)"></div>
  <div class="product-name">Vintage Chalky Paint</div><div class="product-price">KSh $10.00</div>
</div>
<div class="product" style="left:353px">
  <div class="photo" role="img" aria-label="Wooden bone and paw shaped cutouts" style="background:linear-gradient(135deg,#6f6f6f 0%,#c8b08a 45%,#d8c29c 70%,#6a6a6a 100%)"></div>
  <div class="product-name">Wood Cutouts Bundle<br>-Wreath Words</div><div class="product-price">KSh $25.00</div>
</div>
<div class="product" style="left:616px">
  <div class="photo" role="img" aria-label="White ceramic llama planter kit with paints" style="background:linear-gradient(160deg,#f2f2f4 0%,#dcdde2 60%,#c9d6e8 100%)"><span class="add-cart">Add to Cart</span></div>
  <div class="product-name">Llama Ceramic DIY Kit</div><div class="product-price">KSh $28.00</div>
</div>
<div class="product" style="left:879px">
  <div class="photo" role="img" aria-label="Stack of colourful chunky knit yarn skeins" style="background:radial-gradient(circle at 50% 55%,#d84f8c 0%,#6f7fd8 35%,#4fc36a 60%,#ffffff 85%)"></div>
  <div class="product-name">Chunky Knit Yarn</div><div class="product-price">KSh $9.00</div>
</div>

<!-- footer -->
<svg class="band" style="top:3636px" width="1200" height="60" viewBox="0 0 1200 60" preserveAspectRatio="none">
  <polygon points="0,0 1200,55 1200,60 0,60" fill="var(--night)"/>
</svg>
<div class="abs" style="left:0;top:3694px;width:1200px;height:320px;background:var(--night)"></div>
<div class="abs" style="left:0;top:3640px;width:1200px;height:56px;background:var(--night);clip-path:polygon(0 0,100% 100%,0 100%)"></div>
<div class="footer-brand">The Makerloft<br>Barn</div>
<div class="footer-col" style="left:351px">
  <h4>Conatct info</h4>
  <div><span style="color:var(--orange);font-weight:500">Call Us:</span> <span style="font-size:18px">555-014-2290</span></div>
  <div style="font-size:15px;line-height:22px">hello@makerloftbarn.com</div>
  <div style="color:var(--orange);font-weight:500;margin-top:12px;line-height:24px">Address:</div>
  <div style="font-size:13px;line-height:20px">48 Orchard Lane,<br>Millbrook, KY 40099</div>
</div>
<div class="footer-col" style="left:614px">
  <h4>Quick Link</h4>
  <div>Home</div><div>Studio Activities</div><div style="color:var(--blue)">Studio Events</div><div>Resources</div><div>Online Shop</div>
</div>
<div class="footer-col" style="left:879px">
  <h4>Operating Hours</h4>
  <div>Thursday &amp; Friday: 12-6</div><div>Saturday: 10-3</div>
  <h4 style="margin-top:14px;margin-bottom:0">Social Media</h4>
  <div class="social" aria-label="Social media links"><i></i><i></i><i></i><i></i></div>
</div>
<div class="copyright">Copyright © 2021 The Makerloft Barn. All Rights Reserved</div>

</body>
</html>
```